Labels for probiotic care products as Body Cream, Shower gel, Hand soap, ....

We are a starting a business in Flanders Belgium. We are looking for a label for care products, based on probiotics or good bacterie. We are looking for a fresh design that attracts people who wants a good product, based on naturally components. The products make that the microflora of the skin becomes and remains natural. The label must we be adaptive on bottles of 15 cm height to 8 cm height and a width of 4,5 cm. The brand name is KOLA EMU (beautiful skin in Hawaiian) or maybe just KOLA.

Industry/Entity Type

Business

Colors

Designer to choose colors to be used in the design.

Requirements
Must have
• somewhere the text "Probiotic Skin Care"
• I also have to tell that the bottles are white.
Nice to have
• I uploaded the 9 existing labels, but I want a totally new one, because the labels of our cleaning products are the same. I also uploaded a mood bord of labels I like.

```html
<!DOCTYPE html>
<html lang="en">
<head>
<meta charset="utf-8">
<title>KOLA EMU — Probiotic Skin Care Label</title>
<link rel="stylesheet" href="https://fonts.googleapis.com/css2?family=Josefin+Sans:wght@200;300&family=Lato:wght@400&display=swap">
<style>
  :root {
    --backdrop: #d9d9da;
    --label-white: #ffffff;
    --probiotic-blue: #5fb4e0;
    --band-blue: #a6d0e4;
    --ink-grey: #6b6b6b;
    --rule-grey: #8c8c8c;
    --frame-grey: #a7a39b;
    --size-ink: #3f4d55;
    --size-frame: #eaf4f9;
  }
  html, body {
    margin: 0;
    padding: 0;
    width: 1200px;
    height: 1200px;
    overflow: hidden;
    background: var(--backdrop);
  }
  .canvas {
    position: relative;
    width: 1200px;
    height: 1200px;
  }
  .product-label {
    position: absolute;
    left: 300px;
    top: 120px;
    width: 600px;
    height: 960px;
    box-shadow: 0 6px 14px rgba(0,0,0,0.12);
  }
  .title-main { font-family: "Josefin Sans", sans-serif; font-weight: 200; fill: var(--probiotic-blue); }
  .title-sub { font-family: "Josefin Sans", sans-serif; font-weight: 300; fill: var(--ink-grey); }
  .brand-name { font-family: "Josefin Sans", sans-serif; font-weight: 300; fill: var(--ink-grey); }
  .repair-title { font-family: "Josefin Sans", sans-serif; font-weight: 300; fill: var(--ink-grey); }
  .repair-copy { font-family: "Lato", sans-serif; font-weight: 400; fill: #333; }
  .size-copy { font-family: "Lato", sans-serif; font-weight: 400; fill: var(--size-ink); }
</style>
</head>
<body>
<main class="canvas">
  <svg class="product-label" viewBox="0 0 600 960" xmlns="http://www.w3.org/2000/svg">
    <defs>
      <linearGradient id="bubble-fade" x1="0" y1="0" x2="1" y2="0">
        <stop offset="0" stop-color="#ffffff" stop-opacity="0"/>
        <stop offset="1" stop-color="#ffffff" stop-opacity="0.55"/>
      </linearGradient>
    </defs>

    <rect class="label-ground" x="0" y="0" width="600" height="960" fill="var(--label-white)"/>

    <text class="title-main" font-size="136" transform="translate(170 707) rotate(-90)" textLength="652" lengthAdjust="spacingAndGlyphs">PROBIOTIC</text>
    <text class="title-sub" font-size="66" transform="translate(228 707) rotate(-90)" textLength="309" lengthAdjust="spacingAndGlyphs">SKIN CARE</text>

    <line class="divider-rule" x1="246" y1="65" x2="246" y2="711" stroke="var(--rule-grey)" stroke-width="1.5"/>

    <text class="brand-name" x="420" y="305" font-size="40" text-anchor="middle">KOLA EMU</text>

    <g class="repair-panel">
      <rect x="262" y="534" width="318" height="174" fill="none" stroke="var(--frame-grey)" stroke-width="1.5"/>
      <text class="repair-title" x="421" y="577" font-size="34" text-anchor="middle">SKIN REPAIR</text>
      <rect x="268" y="591" width="306" height="55" fill="none" stroke="#e4e2de" stroke-width="1"/>
      <rect x="268" y="649" width="306" height="55" fill="none" stroke="#e4e2de" stroke-width="1"/>
      <text class="repair-copy" x="421" y="614" font-size="23" text-anchor="middle">cream hydratane</text>
      <text class="repair-copy" x="421" y="639" font-size="23" text-anchor="middle">anti age</text>
      <text class="repair-copy" x="421" y="673" font-size="23" text-anchor="middle">anti-again restoration</text>
      <text class="repair-copy" x="421" y="698" font-size="23" text-anchor="middle">misurizer</text>
    </g>

    <rect class="base-band" x="0" y="753" width="600" height="207" fill="var(--band-blue)"/>

    <g class="size-tag">
      <rect x="72" y="842" width="172" height="42" fill="none" stroke="var(--size-frame)" stroke-width="1.5"/>
      <text class="size-copy" x="158" y="870" font-size="23" text-anchor="middle">1.7 oz . 50 ml</text>
    </g>

    <rect class="bubble-field" role="img" aria-label="Decorative scatter of pale bubbles suggesting good bacteria" x="338" y="780" width="262" height="118" fill="url(#bubble-fade)"/>
  </svg>
</main>
</body>
</html>
```